Medical equipment business looking for professional, unique business card

We need a business card design for a durable medical equipment company. We are small but would like our cards to express that we are much bigger. We focus on braces (back, knee, wrist, etc) but also do crutches, rollators, wheelchairs- basically medical equipment that gets you going and back in Action. Our colors are blue and green and our logo has an arrow and use of a "spine". We'd like to express professionalism while being unique.

Industry/Entity Type

Medical Equipment

Contact Information for Business Card

Professional feel but unique. Memorable.

Font styles to use
Serif
Sans Serif
Other font styles liked:
• verdana

Requirements
Must have
• card holders cell#, business phone#, fax#, email, website address, business address, logo
Nice to have
• use of medical/healthcare related descriptive words, items, look
Should not have
• the wrong colors or cartoon characters.

```html
<!DOCTYPE html>
<html lang="en">
<head>
<meta charset="utf-8">
<title>Stride DME – Business Card</title>
<link href="https://fonts.googleapis.com/css2?family=Open+Sans:wght@400;600;700&display=swap" rel="stylesheet">
<style>
  :root {
    --backdrop: #4a4a4a;
    --card-white: #efefef;
    --brand-navy: #1d4f7a;
    --brand-blue: #1a8fcf;
    --brand-green: #8dc63f;
    --ink: #2a2a2a;
    --dot-tint: rgba(255,255,255,0.35);
  }
  * { margin: 0; padding: 0; box-sizing: border-box; }
  html, body { width: 1200px; height: 900px; overflow: hidden; }
  body {
    background: var(--backdrop);
    font-family: "Open Sans", Verdana, sans-serif;
    position: relative;
  }
  .card {
    position: absolute;
    top: 305px;
    width: 500px;
    height: 290px;
    border-radius: 24px;
    overflow: hidden;
    box-shadow: 0 10px 24px rgba(0,0,0,0.35);
  }
  .card--front { left: 70px; background: var(--card-white); }
  .card--back { left: 630px; background: var(--brand-green); }

  .brand { position: absolute; }
  .brand__name {
    font-weight: 600;
    line-height: 1;
    letter-spacing: 0.5px;
  }
  .brand__tagline {
    font-weight: 600;
    margin-top: 6px;
  }
  .card--front .brand { left: 44px; top: 50px; }
  .card--front .brand__name { font-size: 46px; color: var(--brand-navy); }
  .card--front .brand__tagline { font-size: 15px; color: var(--brand-blue); }

  .card--back .brand { left: 0; right: 0; top: 78px; text-align: center; }
  .card--back .brand__name { font-size: 50px; color: var(--brand-blue); }
  .card--back .brand__tagline { font-size: 16px; color: var(--brand-blue); }

  .divider-arrow { position: absolute; left: 286px; top: 110px; }

  .holder { position: absolute; left: 40px; top: 182px; color: var(--ink); }
  .holder__name { font-size: 17px; font-weight: 700; color: var(--brand-blue); }
  .holder__role { font-size: 13px; margin-top: 1px; }
  .holder__address { font-size: 13px; line-height: 1.35; margin-top: 16px; }

  .contacts {
    position: absolute; left: 318px; top: 126px;
    list-style: none; font-size: 13px; color: var(--ink); line-height: 1;
  }
  .contacts li { display: flex; align-items: center; gap: 6px; margin-bottom: 6px; }
  .contacts svg { width: 11px; height: 11px; fill: var(--brand-navy); flex: none; }

  .spine-band {
    position: absolute; left: 0; right: 0; bottom: 0; height: 90px;
    background: linear-gradient(to top, var(--dot-tint), rgba(255,255,255,0));
  }
</style>
</head>
<body>

<section class="card card--front">
  <div class="brand">
    <div class="brand__name">Stride DME</div>
    <div class="brand__tagline">Durable Medical Equipment</div>
  </div>

  <svg class="divider-arrow" width="20" height="180" viewBox="0 0 20 180">
    <line x1="10" y1="178" x2="10" y2="6" stroke="#8dc63f" stroke-width="1.6"/>
    <path d="M5 10 L10 2 L15 10" fill="none" stroke="#8dc63f" stroke-width="1.6"/>
  </svg>

  <ul class="contacts">
    <li><svg viewBox="0 0 12 12"><path d="M1 4 Q6 0 11 4 L9 6 L8 4.5 H4 L3 6 Z M3 7 H9 V11 H3 Z"/></svg>+ 61 400 000 111</li>
    <li><svg viewBox="0 0 12 12"><rect x="3" y="0.5" width="6" height="11" rx="1"/></svg>+ 61 2 9000 1234</li>
    <li><svg viewBox="0 0 12 12"><rect x="1" y="4" width="10" height="7" rx="1"/><rect x="3" y="1" width="6" height="3"/></svg>(402)-55-789</li>
    <li><svg viewBox="0 0 12 12"><path d="M1 2.5 H11 V10 H1 Z M1 2.5 L6 7 L11 2.5" /></svg>hello@stridedme.com</li>
    <li><svg viewBox="0 0 12 12"><circle cx="6" cy="6" r="5.5"/></svg>www.stridedme.co</li>
  </ul>

  <div class="holder">
    <div class="holder__name">Dana Whitfield</div>
    <div class="holder__role">Marketing</div>
    <div class="holder__address">Suite 8, Level 2, 41 Harbour Lane,<br>Sydney, NSW, 2000, Australia</div>
  </div>
</section>

<section class="card card--back">
  <div class="brand">
    <div class="brand__name">Stride DME</div>
    <div class="brand__tagline">Durable Medical Equipment</div>
  </div>
  <div class="spine-band" role="img" aria-label="Decorative row of pale vertebra-like dots sweeping across the card"></div>
</section>

</body>
</html>
```